New Business Card Design Project - RK Ledgerwise & Filing Partners, LLC

Below is a sample image of the card (TM Bookkeeping). I would like to have a designed business card that looks very similar (Front & Back). In addition, I would like to keep the same colors as well. I attached my Business Logo (RK Ledgerwise & Filing Partners, LLC) that will be on my website.

Target Market(s)

Executives, Business Owners, Board of Directors, Chief Financial Officers

Contact Information for Business Card

Font styles to use
Serif

Colors
0c5ba6
ffffff
5c5c5c

Requirements
Must have
• My Name: Malcolm Ferris, CPA
• Position: Owner
• Phone: (240) 555-0148
• Email: Mferris@rkledgerwise.example
• Website: www.Rkledgerwise.example
• Address: 4736 Ferncliff Ave #2093
• Dunmore Falls, MD 21990
Nice to have
• Same design & color scheme as TM Bookkeepnig Business card sample attached

```html
<!DOCTYPE html>
<html lang="en">
<head>
<meta charset="utf-8">
<title>RK Ledgerwise – Business Card</title>
<link href="https://fonts.googleapis.com/css2?family=Cinzel:wght@400;500&family=Lato:wght@400&display=swap" rel="stylesheet">
<style>
  :root {
    --brand-blue: #1ab0dc;
    --brand-gray: #5c5c5c;
    --text-dark: #2e2e2e;
    --card-white: #f7f7f7;
    --backdrop: #e6e6e6;
    --white: #ffffff;
  }
  * { margin: 0; padding: 0; box-sizing: border-box; }
  html, body { width: 1200px; height: 802px; overflow: hidden; background: var(--backdrop); }
  .stage { position: relative; width: 1200px; height: 802px; }

  .card {
    position: absolute;
    top: 274px;
    width: 443px;
    height: 265px;
    box-shadow: 0 2px 6px rgba(0,0,0,0.18);
    overflow: hidden;
  }
  .card--front { left: 136px; background: var(--card-white); }
  .card--back { left: 624px; background: var(--brand-blue); }

  /* Front */
  .brand {
    position: absolute;
    left: 26px;
    top: 120px;
    display: flex;
    align-items: center;
    gap: 8px;
  }
  .brand__dot { width: 14px; height: 14px; border-radius: 50%; background: var(--brand-blue); }
  .brand__name {
    font-family: "Cinzel", serif;
    font-size: 15px;
    letter-spacing: 1.2px;
    color: var(--brand-blue);
  }
  .divider {
    position: absolute;
    left: 217px;
    top: 69px;
    width: 1px;
    height: 122px;
    background: #cfcfcf;
  }
  .contact {
    position: absolute;
    left: 241px;
    top: 71px;
    font-family: "Lato", sans-serif;
    color: var(--text-dark);
  }
  .contact__name {
    font-family: "Cinzel", serif;
    font-size: 17px;
    line-height: 20px;
    color: var(--brand-blue);
    white-space: nowrap;
  }
  .contact__credential { color: var(--brand-gray); }
  .contact__title { font-size: 13px; line-height: 16px; margin-top: 1px; }
  .contact__list { list-style: none; margin-top: 7px; }
  .contact__item {
    display: flex;
    align-items: center;
    gap: 3px;
    font-size: 13px;
    line-height: 16px;
  }
  .contact__icon { width: 11px; height: 11px; flex: none; }
  .contact__address { font-size: 13px; line-height: 16px; margin-top: 8px; font-style: normal; }

  .accent-band { position: absolute; left: 0; bottom: 0; width: 100%; height: 14px; display: flex; }
  .accent-band__blue { width: 270px; background: var(--brand-blue); }
  .accent-band__gray { flex: 1; background: var(--brand-gray); }

  /* Back */
  .back-brand {
    position: absolute;
    left: 0; right: 0;
    top: 118px;
    display: flex;
    justify-content: center;
    align-items: center;
    gap: 9px;
  }
  .back-brand__dot { width: 16px; height: 16px; border-radius: 50%; background: var(--white); }
  .back-brand__name {
    font-family: "Cinzel", serif;
    font-size: 15px;
    letter-spacing: 1.3px;
    color: var(--white);
    white-space: nowrap;
  }
  .back-web {
    position: absolute;
    left: 0; right: 0;
    top: 198px;
    text-align: center;
    font-family: "Lato", sans-serif;
    font-size: 12.5px;
    color: var(--white);
  }
</style>
</head>
<body>
<main class="stage">
  <section class="card card--front" aria-label="Card front">
    <div class="brand">
      <span class="brand__dot"></span>
      <span class="brand__name">RK LEDGERWISE</span>
    </div>
    <div class="divider"></div>
    <div class="contact">
      <p class="contact__name">Malcolm Ferris, <span class="contact__credential">CPA</span></p>
      <p class="contact__title">Owner</p>
      <ul class="contact__list">
        <li class="contact__item">
          <svg class="contact__icon" viewBox="0 0 12 12" aria-hidden="true"><path fill="#1ab0dc" d="M1 4c0-2 2-3 5-3s5 1 5 3v1H8V4H4v1H1zM3 6h6l1.5 4.5h-9z"/></svg>
          (240) 555-0148
        </li>
        <li class="contact__item">
          <svg class="contact__icon" viewBox="0 0 12 12" aria-hidden="true"><rect x="0.5" y="2.5" width="11" height="7.5" fill="#1ab0dc"/><path d="M1 3l5 4 5-4" fill="none" stroke="#fff" stroke-width="1"/></svg>
          Mferris@rkledgerwise.example
        </li>
        <li class="contact__item">
          <svg class="contact__icon" viewBox="0 0 12 12" aria-hidden="true"><circle cx="6" cy="6" r="5.2" fill="#1ab0dc"/><path d="M3 4.5c1.5 0 2 1 1.5 2.5M7.5 2.5c0 1.5 1.5 1.5 2 3M6.5 9c.5-1.5 2-1.5 2.5-1" fill="none" stroke="#fff" stroke-width="0.9"/></svg>
          www.Rkledgerwise.example
        </li>
      </ul>
      <address class="contact__address">4736 Ferncliff Ave #2093<br>Dunmore Falls, MD 21990</address>
    </div>
    <div class="accent-band"><span class="accent-band__blue"></span><span class="accent-band__gray"></span></div>
  </section>

  <section class="card card--back" aria-label="Card back">
    <div class="back-brand">
      <span class="back-brand__dot"></span>
      <span class="back-brand__name">RK LEDGERWISE &amp; FILING PARTNERS</span>
    </div>
    <p class="back-web">www.rkledgerwise.example</p>
  </section>
</main>
</body>
</html>
```